Business Card for Polygraph business in Africa

Business Card . Polygraph Examiner based in Tanzania, East Africa.
Business Card will be used to disseminate contact information to potential clients.
It should convey that I am a professional specifically in the polygraph field and perform my work with integrity.

I have attached the business card that I'm currently using, which I threw together myself initially. It's not professional enough.

Target Market(s)

Banks, Accounting Firms, Government Ministries, Gas, Oil, & Gemstone Mining Concerns, Wildlife Conservation NGOs, International companies located in East Africa.

Industry/Entity Type

Business

Contact Information for Business Card

Veritas Lumeno
Harriet Munsell
PO Box 48317
Arusha, Tanzania
+255 712 839 254
harrietmunsell@quillpost.example

Colors
00a990
f37122
faa54b

Requirements
Must have
• - Veritas Lumeno (with the word "Polygraph" being more prominent than the word "Tanzania")
• - Forensic Examinations
• - Employment Screening
• - Should contain a logo of the Continental Truthfinder Guild (of which I'm a member)
• - I would like an accent design (such as the polygraph "squiggles" of a cardio tracing or such as that)
• - My contact information (less prominent, but large enough to read legibly). I would also consider putting the contact information on the second side of the card.
Nice to have
• My color suggestions are changeable.
Should not have
• Anything "cutesy" or "cartoonish"

```html
<!DOCTYPE html>
<html lang="en">
<head>
<meta charset="utf-8">
<title>Veritas Lumeno — Business Card</title>
<link href="https://fonts.googleapis.com/css2?family=Open+Sans:wght@400;600&display=swap" rel="stylesheet">
<style>
  :root {
    --backdrop: #2a2a2b;
    --card: #5e5f5e;
    --card-edge: #545554;
    --ink-light: #c9cac9;
    --ink-soft: #b5b6b5;
    --teal: #13a88f;
    --orange: #f07a2b;
    --seal: #d9d9d9;
  }
  * { box-sizing: border-box; margin: 0; padding: 0; }
  html, body {
    width: 1200px; height: 900px; overflow: hidden;
    background: var(--backdrop);
    font-family: "Open Sans", Arial, sans-serif;
  }
  .canvas { position: relative; width: 1200px; height: 900px; }
  .card {
    position: absolute;
    width: 560px; height: 320px;
    background: linear-gradient(160deg, var(--card) 0%, var(--card-edge) 100%);
    border-radius: 22px;
    overflow: hidden;
  }
  .card--front { left: 70px; top: 70px; }
  .card--back { left: 570px; top: 510px; }

  .wordmark {
    position: absolute;
    display: flex; align-items: center; gap: 12px;
    color: var(--ink-light);
    font-weight: 400; letter-spacing: 0.5px;
    white-space: nowrap;
  }
  .wordmark__dot {
    width: 14px; height: 14px; border-radius: 50%;
    background: var(--orange);
    flex: none;
  }
  .card--front .wordmark { left: 0; right: 0; justify-content: center; top: 118px; font-size: 46px; }
  .card--back .wordmark { left: 32px; top: 142px; font-size: 24px; gap: 10px; }
  .card--back .wordmark__dot { width: 12px; height: 12px; }

  .seal {
    position: absolute; right: 34px; top: 26px;
    width: 74px; height: 74px; border-radius: 50%;
    border: 3px solid var(--seal);
    background: #6a6b6a;
  }
  .services {
    position: absolute; left: 0; right: 0; top: 222px;
    text-align: center; color: var(--ink-light);
    font-size: 17px; letter-spacing: 0.4px;
  }
  .services__sep { margin: 0 16px; }

  .divider {
    position: absolute; left: 262px; top: 48px;
    width: 2px; height: 224px; background: var(--orange);
  }
  .contact {
    position: absolute; left: 282px; right: 20px; top: 60px;
    color: var(--ink-soft);
  }
  .contact__name { font-size: 21px; color: var(--ink-light); margin-bottom: 18px; white-space: nowrap; }
  .contact__row {
    display: flex; align-items: flex-start; gap: 9px;
    font-size: 13px; line-height: 1.4; margin-bottom: 12px;
    white-space: nowrap;
  }
  .contact__icon { width: 13px; height: 13px; flex: none; margin-top: 2px; }
</style>
</head>
<body>
<main class="canvas">
  <section class="card card--front" aria-label="Card front">
    <div class="seal" role="img" aria-label="Continental Truthfinder Guild membership seal"></div>
    <div class="wordmark"><span class="wordmark__dot"></span>Veritas Lumeno</div>
    <p class="services">Issue investigation<span class="services__sep">|</span>Employment screening</p>
  </section>

  <section class="card card--back" aria-label="Card back">
    <div class="wordmark"><span class="wordmark__dot"></span>Veritas Lumeno</div>
    <div class="divider"></div>
    <div class="contact">
      <p class="contact__name">Harriet Munsell</p>
      <div class="contact__row">
        <svg class="contact__icon" viewBox="0 0 14 14" aria-hidden="true"><path d="M7 1a4 4 0 0 0-4 4c0 3 4 8 4 8s4-5 4-8a4 4 0 0 0-4-4z" fill="var(--teal)"/><circle cx="7" cy="5" r="1.5" fill="var(--card)"/></svg>
        <span>PO Box 48317<br>Arusha, Tanzania</span>
      </div>
      <div class="contact__row">
        <svg class="contact__icon" viewBox="0 0 14 14" aria-hidden="true"><path d="M3 1.5l2 .2 1 3-1.4 1a7 7 0 0 0 3.7 3.7l1-1.4 3 1 .2 2c0 .8-.8 1.5-1.6 1.4A11 11 0 0 1 1.6 3.1C1.5 2.3 2.2 1.5 3 1.5z" fill="var(--teal)"/></svg>
        <span>+255 712 839 254</span>
      </div>
      <div class="contact__row">
        <svg class="contact__icon" viewBox="0 0 14 14" aria-hidden="true"><rect x="1" y="3" width="12" height="8.5" rx="1" fill="var(--teal)"/><path d="M1.5 3.6L7 8l5.5-4.4" fill="none" stroke="var(--card)" stroke-width="1.1"/></svg>
        <span>harrietmunsell@quillpost.example</span>
      </div>
    </div>
  </section>
</main>
</body>
</html>
```